Geschäftspapiere für Praxis für Integrative Physiotherapie
Zielgruppe
Praxis für Integrative Physiotherapie
Aufgabenstellung
Edel und übersichtlich, gern mit Farbe. Eventuell ein Wasserzeichen.
Logo gern in Relieflack oder als Metallic-Effekt gedruckt. Das neue Logo wurde bereits erstellt und befindet sich im Anhang! Im Anhang auch ein Bild von den aktuellen Visitenkarten!

```html
<!DOCTYPE html>
<html lang="de">
<head>
<meta charset="utf-8">
<title>Briefbogen – Zentrum Birkenhain</title>
<link href="https://fonts.googleapis.com/css2?family=Josefin+Sans:wght@400;600;700&display=swap" rel="stylesheet">
<style>
  :root {
    --orange: #f5ac5e;
    --orange-text: #e8873a;
    --soft: #f9e2cf;
    --ink: #1a1a1a;
    --mark: #8a8a8a;
    --bg: #ffffff;
  }
  html, body { margin: 0; padding: 0; overflow: hidden; }
  body {
    width: 1200px; height: 1200px; background: var(--bg);
    font-family: "Josefin Sans", sans-serif; color: var(--ink);
    position: relative;
  }
  .sheet {
    position: absolute; left: 288px; top: 174px; width: 632px; height: 892px;
    background: #fff; overflow: hidden;
    box-shadow: 0 1px 4px rgba(0,0,0,.35);
  }
  .sheet-deco { position: absolute; inset: 0; }
  .brand { position: absolute; right: 59px; top: 64px; text-align: right; }
  .brand-name { font-size: 27px; font-weight: 600; color: var(--orange-text); line-height: 1; }
  .brand-tagline { font-size: 12.5px; font-weight: 600; margin-top: 16px; letter-spacing: .3px; }
  .sender-line { position: absolute; left: 75px; top: 145px; font-size: 7.5px; }
  .practitioner { position: absolute; right: 59px; top: 140px; text-align: right; font-size: 11.5px; line-height: 14.5px; }
  .practitioner-name { font-weight: 700; font-size: 12px; }
  .footer { position: absolute; left: 0; top: 820px; width: 100%; font-size: 5.6px; font-weight: 600; line-height: 9px; }
  .footer-col { position: absolute; top: 0; }
  .footer-title { color: var(--orange); font-weight: 400; font-size: 7px; margin-bottom: 1px; }
  .contact { left: 76px; }
  .bank { left: 244px; }
  .hours { left: 412px; }
  .contact-row { position: relative; }
  .contact-icon { position: absolute; left: -14px; top: 1px; width: 6px; height: 6px; }
  .hours-row span { display: inline-block; width: 46px; }
</style>
</head>
<body>
  <main class="sheet">
    <svg class="sheet-deco" width="632" height="892" viewBox="0 0 632 892">
      <defs>
        <radialGradient id="soft-glow" cx="50%" cy="40%" r="60%">
          <stop offset="0" stop-color="#fdf1e6"/>
          <stop offset="1" stop-color="#f8dcc6"/>
        </radialGradient>
      </defs>
      <path class="corner-top" d="M0 0 H251 Q90 25 0 86 Z" fill="var(--orange)"/>
      <path class="corner-bottom" d="M378 892 Q540 875 632 806 V892 Z" fill="var(--orange)"/>
      <circle role="img" aria-label="Dekoratives Praxiszeichen, dezent hinter dem Namen" cx="569" cy="68" r="68" fill="url(#soft-glow)" opacity=".55"/>
      <circle role="img" aria-label="Großes Praxiszeichen als Wasserzeichen" cx="190" cy="538" r="241" fill="url(#soft-glow)" opacity=".5"/>
      <g class="fold-marks" stroke="var(--mark)">
        <line x1="0" y1="322" x2="11" y2="322" stroke-width="1.2"/>
        <line x1="0" y1="451" x2="11" y2="451" stroke-width="2"/>
        <line x1="0" y1="634" x2="11" y2="634" stroke-width="1.2"/>
      </g>
    </svg>

    <header class="brand">
      <div class="brand-name">Zentrum Birkenhain</div>
      <div class="brand-tagline">Praxis für integrative Physiotherapie</div>
    </header>

    <div class="sender-line">Zentrum Birkenhain | Lindenweg 12 | 15370 Birkenhain</div>

    <div class="practitioner">
      <div class="practitioner-name">Jonas Falkenried</div>
      <div>Physiotherapeut</div>
      <div>Masseur u. med. Bademeister</div>
      <div>Yogalehrer</div>
    </div>

    <footer class="footer">
      <div class="footer-col contact">
        <div class="footer-title">KONTAKT</div>
        <div class="contact-row"><svg class="contact-icon" viewBox="0 0 10 10"><path d="M5 0a3.5 3.5 0 0 0-3.5 3.5C1.5 6 5 10 5 10s3.5-4 3.5-6.5A3.5 3.5 0 0 0 5 0z" fill="var(--orange)"/></svg>Lindenweg 12 | 15370 Birkenhain</div>
        <div class="contact-row"><svg class="contact-icon" viewBox="0 0 10 10"><path d="M2 1l2 2-1 1.5c.8 1.5 1.8 2.5 3 3L7.5 6l2 2-1.5 1.5C4 9 1 6 .5 2.5z" fill="none" stroke="var(--orange)"/></svg>033430 51827</div>
        <div class="contact-row"><svg class="contact-icon" viewBox="0 0 10 10"><rect x="2.5" y="0.5" width="5" height="3" fill="none" stroke="var(--orange)"/><rect x="0.5" y="3.5" width="9" height="4" fill="var(--orange)"/><rect x="2.5" y="7" width="5" height="2.5" fill="none" stroke="var(--orange)"/></svg>033430 518290</div>
        <div class="contact-row"><svg class="contact-icon" viewBox="0 0 10 10"><rect x="0.5" y="2" width="9" height="6" fill="none" stroke="var(--orange)"/><path d="M.5 2L5 5.5 9.5 2" fill="none" stroke="var(--orange)"/></svg>praxis@zentrum-birkenhain.de</div>
        <div class="contact-row"><svg class="contact-icon" viewBox="0 0 10 10"><path d="M10 0L0 4l4 2 2 4z" fill="var(--orange)"/></svg>www.zentrum-birkenhain.de</div>
      </div>
      <div class="footer-col bank">
        <div class="footer-title">KREDITINSTITUT</div>
        <div>Kreissparkasse Oderland</div>
        <div>IBAN: DE12 1705 0000 0031 4159 26</div>
        <div>BIC: ODERDEF1KSO</div>
        <div>St-Nr.: 061 558 02917</div>
        <div>IK - Nr.: 440738612</div>
      </div>
      <div class="footer-col hours">
        <div class="footer-title">THERAPIEZEITEN</div>
        <div class="hours-row"><span>Montags</span>8:00 - 18:30</div>
        <div class="hours-row"><span>Dienstags</span>8:00 - 18:00</div>
        <div class="hours-row"><span>Mittwochs</span>8:00 - 18:30</div>
        <div class="hours-row"><span>Donnerstags</span>8:00 - 18:00</div>
        <div class="hours-row"><span>Freitags</span>8:00 - 13:00</div>
      </div>
    </footer>
  </main>
</body>
</html>
```